Marrowind Labs - pioneers of next generation consulting!

We are a next generation management consulting firm with two focus areas and USPs (unique selling points):>Technology driven business developmentWe are not developers, we are experts in HOW to apply and incorporate technology in your business dna to drive business growth and value-added change.>Creating high performing teams levering our philosophy of collective intelligence. We truly understand the need of human engagement and we know that the only way of getting there is by building strong relationships among people, a warm and open culture is a stepping stone towards effective collaboration within/among teams. - We don't want a ”corporate feel” to our templates. The organic feeling we have with our blue-on-blue blobs has the idea of ever changing movement and shape changing. Please see our website, www.marrowindlabs.se. - In our context we sit among classic business mgmt. consultants and classic IT mgmt. consultants. We cater to business, tech and humans as the ultimate vehicle of change and business value. -To have a clean template one suggestion is to only use blue, white and black and keeping other colors separate, as an alternative but we are truly open allow your creativity add value to this. We are looking to find a slide deck which we can pick slides from, depending on what/whom/why we interact with customer we want to create different outcomes and our presentations should support this.

Industry/Entity Type

Management Consulting

Requirements
Must have
• next generation powerpoint and how to package storytelling. please keep to our look and feel, we just arrived at our logo, colours and shapes. Help us to carry it into our ppt's as well.
Should not have
• Hi all, please have a look at our website. It is still very new and more will be done, but our goal is to make powerpoint to come alive again and mirror our pioneering hearts and brains.

```html
<!DOCTYPE html>
<html lang="en">
<head>
<meta charset="utf-8">
<title>About This Design – Marrowind Labs</title>
<link href="https://fonts.googleapis.com/css2?family=Permanent+Marker&family=Cousine&family=Montserrat:wght@600&display=block" rel="stylesheet">
<style>
  :root {
    --paper: #ffffff;
    --ink: #111111;
    --muted: #8a8a8a;
    --navy: #1b3566;
    --royal: #1f4f9c;
    --sky: #2e7fd6;
    --charcoal: #262626;
    --green: #3cb44b;
    --band-dark: #0d4f9a;
    --band-light: #4aa3e6;
    --area-outer: #4f6f9f;
    --area-mid: #3a6fb8;
    --area-inner: #2f7fd0;
    --area-core: #3fae9a;
  }
  html, body {
    margin: 0;
    padding: 0;
    overflow: hidden;
    background: var(--paper);
  }
  .slide {
    position: relative;
    width: 1200px;
    height: 687px;
    overflow: hidden;
    background: var(--paper);
  }
  .slide-title {
    position: absolute;
    top: 44px;
    left: 0;
    width: 1150px;
    margin: 0;
    text-align: center;
    font-family: "Permanent Marker", "Marker Felt", "Comic Sans MS", cursive;
    font-weight: 400;
    font-size: 36px;
    line-height: 50px;
    letter-spacing: 1px;
    text-transform: uppercase;
    color: var(--ink);
  }
  .point-list {
    list-style: none;
    margin: 0;
    padding: 0;
  }
  .point {
    position: absolute;
    display: flex;
    align-items: center;
    height: 48px;
    font-family: "Cousine", "Liberation Mono", monospace;
    color: var(--ink);
    white-space: nowrap;
  }
  .point-marker {
    flex: none;
    margin-right: 18px;
  }
  .point--1 { left: 177px; top: 132px; font-size: 34px; }
  .point--2 { left: 134px; top: 192px; font-size: 34px; }
  .point--3 { left: 92px;  top: 253px; font-size: 29px; }
  .point--4 { left: 59px;  top: 311px; font-size: 26px; }
  .point--5 { left: 26px;  top: 376px; font-size: 26px; }
  .point--1 .point-marker { margin-right: 20px; }
  .point--4 .point-marker { margin-right: 14px; }
  .point--5 .point-marker { margin-right: 14px; }
  .target-illustration {
    position: absolute;
    left: 480px;
    top: 186px;
    width: 712px;
    height: 390px;
  }
  .page-number {
    position: absolute;
    left: 40px;
    top: 594px;
    font-family: "Montserrat", sans-serif;
    font-size: 16px;
    color: var(--muted);
  }
  .footer-band {
    position: absolute;
    left: 0;
    top: 623px;
    width: 1200px;
    height: 50px;
  }
  .brand-name {
    position: absolute;
    right: 37px;
    top: 636px;
    font-family: "Montserrat", sans-serif;
    font-weight: 600;
    font-size: 22px;
    letter-spacing: 0.5px;
    text-transform: uppercase;
    color: var(--paper);
  }
</style>
</head>
<body>
<main class="slide">
  <h1 class="slide-title">About This Design</h1>

  <ul class="point-list">
    <li class="point point--1">
      <svg class="point-marker" width="47" height="47" viewBox="0 0 47 47"><polygon points="2,2 45,23.5 2,45" fill="var(--navy)"/></svg>
      Use of new fonts
    </li>
    <li class="point point--2">
      <svg class="point-marker" width="48" height="48" viewBox="0 0 48 48"><polygon points="2,2 46,24 2,46" fill="var(--royal)"/></svg>
      New designer
    </li>
    <li class="point point--3">
      <svg class="point-marker" width="48" height="48" viewBox="0 0 48 48"><polygon points="2,2 46,24 2,46" fill="var(--sky)"/></svg>
      Feedback requested
    </li>
    <li class="point point--4">
      <svg class="point-marker" width="48" height="48" viewBox="0 0 48 48"><polygon points="2,2 46,24 2,46" fill="var(--charcoal)"/></svg>
      hello@fernlab.net
    </li>
    <li class="point point--5">
      <svg class="point-marker" width="48" height="48" viewBox="0 0 48 48"><polygon points="2,2 46,24 2,46" fill="var(--green)"/></svg>
      Can help further
    </li>
  </ul>

  <svg class="target-illustration" role="img" aria-label="Illustration area: layered blue rings around a green centre with a small flag, a target metaphor" viewBox="0 0 712 390">
    <defs>
      <radialGradient id="targetTones" cx="0.5" cy="0.45" r="0.65">
        <stop offset="0" stop-color="var(--area-core)"/>
        <stop offset="0.35" stop-color="var(--area-inner)"/>
        <stop offset="0.7" stop-color="var(--area-mid)"/>
        <stop offset="1" stop-color="var(--area-outer)"/>
      </radialGradient>
    </defs>
    <rect width="712" height="390" rx="48" fill="url(#targetTones)"/>
  </svg>

  <div class="page-number">5</div>

  <svg class="footer-band" viewBox="0 0 1200 50" preserveAspectRatio="none" aria-hidden="true">
    <defs>
      <linearGradient id="bandTones" x1="0" y1="0" x2="0" y2="1">
        <stop offset="0" stop-color="var(--band-light)"/>
        <stop offset="1" stop-color="var(--band-dark)"/>
      </linearGradient>
    </defs>
    <rect width="1200" height="50" fill="url(#bandTones)"/>
    <path d="M0,16 C300,4 700,28 1200,9" stroke="var(--paper)" stroke-opacity="0.35" stroke-width="2" fill="none"/>
  </svg>
  <div class="brand-name">Marrowind Labs</div>
</main>
</body>
</html>
```